Vintage-style label for a tube cake pan

We are looking for designs for a 1950-1960s vintage-style label for a cake pan. I've attached examples from other older cake pans. The last two photos are the image we've identified as the one that best encapsulates our brand and an illustration of the pan.

You can leave a placeholder for the logo, and you can use the words below in your design (feel free to pick and choose):

Product title:
Square Tube Cake Pan
Product subtitle:
for Angel Food Cakes and Mile High Pound Cakes
Product Attributes:
Holds 18 cups of batter for mile high cakes
Even-heating aluminum for the highest rise
Resists rust and abrasions
Family-owned and operated company
Two pieces for easy removal
9 in x 9 in x 4.5 in
For recipes and care instructions SEE REVERSE SIDE

The dimensions for the label are 7.5 in x 7.5 in with a 2.4 in hole in the center
Updates

Designs look the same

Target Market(s)

American grandmas

Requirements
Must have
• Should feel authentically vintage to American ads in the 1950s and 1960s

```html
<!DOCTYPE html>
<html lang="en">
<head>
<meta charset="utf-8">
<title>Square Tube Cake Pan Label</title>
<link href="https://fonts.googleapis.com/css2?family=Anton&family=Montserrat:wght@500;700&family=Oswald:wght@500&family=Archivo:wght@800&display=swap" rel="stylesheet">
<style>
  :root {
    --bg-brown: #3a1a18;
    --ink: #2a1414;
    --paper: #f0e6c0;
    --paper-edge: #a87858;
    --orange: #d48a4a;
    --ribbon: #8eae98;
    --white: #ffffff;
    --steel-light: #cfcbc2;
    --steel-dark: #8f8a80;
    --cake: #d9c596;
  }
  html, body { margin: 0; padding: 0; overflow: hidden; background: var(--bg-brown); }
  .label { width: 1200px; height: 1200px; display: block; }
  .title { font-family: "Anton", sans-serif; font-size: 158px; }
  .title-main { fill: var(--ink); }
  .title-shadow { fill: var(--orange); }
  .subtitle { font-family: "Montserrat", sans-serif; font-weight: 500; font-size: 70px; fill: var(--orange); letter-spacing: 4px; }
  .ribbon-text { font-family: "Montserrat", sans-serif; font-weight: 700; font-size: 44px; fill: var(--white); }
  .attr-heading { font-family: "Archivo", sans-serif; font-weight: 800; font-size: 33px; fill: var(--orange); }
  .attr-item { font-family: "Oswald", sans-serif; font-weight: 500; font-size: 31px; fill: var(--ink); }
  .bullet { fill: var(--ink); }
  .reverse-note { font-family: "Oswald", sans-serif; font-weight: 500; font-size: 34px; fill: var(--orange); }
</style>
</head>
<body>
<svg class="label" viewBox="0 0 1200 1200" xmlns="http://www.w3.org/2000/svg">
  <defs>
    <linearGradient id="panTone" x1="0" y1="0" x2="1" y2="1">
      <stop offset="0" stop-color="var(--steel-light)"/>
      <stop offset="0.45" stop-color="var(--cake)"/>
      <stop offset="1" stop-color="var(--steel-dark)"/>
    </linearGradient>
  </defs>

  <rect class="background" width="1200" height="1200" fill="var(--bg-brown)"/>
  <rect class="inner-rule" x="32" y="32" width="1136" height="1136" rx="24" fill="none" stroke="#4a2624" stroke-width="2" stroke-dasharray="3 5"/>

  <g class="torn-paper">
    <polygon transform="translate(-8,10)" fill="var(--paper-edge)" points="90,110 130,95 150,108 175,88 210,100 240,80 270,96 300,78 340,92 370,70 400,88 440,74 470,90 510,66 545,84 580,72 620,88 650,64 690,80 730,70 760,86 800,62 840,80 870,70 905,84 940,60 980,78 1010,68 1050,84 1080,70 1120,82 1135,100 1125,140 1140,180 1120,220 1138,260 1118,300 1134,340 1122,390 1140,430 1118,470 1136,520 1120,560 1142,610 1122,650 1138,700 1118,740 1136,790 1120,840 1140,880 1118,930 1136,980 1122,1030 1138,1080 1120,1120 1080,1130 1040,1118 1000,1136 960,1120 920,1138 880,1116 840,1134 800,1118 760,1140 720,1120 680,1134 640,1116 600,1138 560,1120 520,1136 480,1118 440,1140 400,1120 360,1134 320,1116 280,1138 240,1120 200,1134 160,1118 120,1136 88,1115 75,1080 92,1040 70,1000 90,960 72,920 94,880 68,840 90,800 74,760 96,720 70,680 92,640 72,600 94,560 68,520 90,480 74,440 96,400 70,360 92,320 72,280 94,240 70,200 92,160 78,130"/>
    <polygon fill="var(--paper)" points="90,110 130,95 150,108 175,88 210,100 240,80 270,96 300,78 340,92 370,70 400,88 440,74 470,90 510,66 545,84 580,72 620,88 650,64 690,80 730,70 760,86 800,62 840,80 870,70 905,84 940,60 980,78 1010,68 1050,84 1080,70 1120,82 1135,100 1125,140 1140,180 1120,220 1138,260 1118,300 1134,340 1122,390 1140,430 1118,470 1136,520 1120,560 1142,610 1122,650 1138,700 1118,740 1136,790 1120,840 1140,880 1118,930 1136,980 1122,1030 1138,1080 1120,1120 1080,1130 1040,1118 1000,1136 960,1120 920,1138 880,1116 840,1134 800,1118 760,1140 720,1120 680,1134 640,1116 600,1138 560,1120 520,1136 480,1118 440,1140 400,1120 360,1134 320,1116 280,1138 240,1120 200,1134 160,1118 120,1136 88,1115 75,1080 92,1040 70,1000 90,960 72,920 94,880 68,840 90,800 74,760 96,720 70,680 92,640 72,600 94,560 68,520 90,480 74,440 96,400 70,360 92,320 72,280 94,240 70,200 92,160 78,130"/>
  </g>

  <g class="product-title">
    <text class="title title-shadow" x="273" y="296" textLength="680" lengthAdjust="spacingAndGlyphs">SQUARE TUBE</text>
    <text class="title title-main" x="267" y="290" textLength="680" lengthAdjust="spacingAndGlyphs">SQUARE TUBE</text>
    <text class="subtitle" x="610" y="348" text-anchor="middle">CAKE PAN</text>
  </g>

  <g class="subtitle-ribbon">
    <polygon fill="var(--ribbon)" points="255,368 935,368 905,433 935,500 255,500 290,433"/>
    <polygon fill="none" stroke="var(--white)" stroke-width="1.5" stroke-dasharray="2 3" points="268,376 922,376 895,433 922,492 268,492 298,433"/>
    <text class="ribbon-text" x="590" y="418" text-anchor="middle">for Angel Food Cakes &amp;</text>
    <text class="ribbon-text" x="598" y="470" text-anchor="middle">Mile High Pound Cakes</text>
  </g>

  <g class="product-attributes">
    <text class="attr-heading" x="166" y="606">PRODUCT ATTRIBUTES:</text>
    <g class="attr-list">
      <rect class="bullet" x="148" y="627" width="7" height="7"/>
      <text class="attr-item" x="163" y="649">Holds 18 cups of batter for mile high cakes</text>
      <rect class="bullet" x="148" y="675" width="7" height="7"/>
      <text class="attr-item" x="163" y="697">Even-heating aluminum for the highest rise</text>
      <rect class="bullet" x="148" y="723" width="7" height="7"/>
      <text class="attr-item" x="163" y="745">Resists rust and abrasions</text>
      <rect class="bullet" x="148" y="771" width="7" height="7"/>
      <text class="attr-item" x="163" y="793">Family-owned and operated company</text>
      <rect class="bullet" x="148" y="819" width="7" height="7"/>
      <text class="attr-item" x="163" y="841">Two pieces for easy removal</text>
      <rect class="bullet" x="148" y="867" width="7" height="7"/>
      <text class="attr-item" x="163" y="889">9 in x 9 in x 4.5 in</text>
    </g>
    <text class="reverse-note" x="162" y="950">For recipes and care instructions</text>
    <text class="reverse-note" x="162" y="1004">SEE REVERSE SIDE</text>
  </g>

  <path class="pan-photo" role="img" aria-label="Photo of a baked pound cake in the square aluminum tube pan" fill="url(#panTone)" d="M640,750 Q645,720 680,712 L1040,665 Q1075,662 1090,690 L1112,760 L1100,1000 Q1095,1030 1060,1040 L935,1070 Q900,1075 880,1058 L705,950 Q690,940 688,920 Z"/>
</svg>
</body>
</html>
```